copper meadow

It is a small business that is looking to sell medical supplies and services. later down the line it will branch off to help solve other world problems, i.e. global warming and raw material shortages.
but we will start with hospital equipment and supplies.

Target Market(s)

all medical facilities

Coding

Coded - Design and coding required

Number of Pages Required

1 page

```html
<!DOCTYPE html>
<html lang="en">
<head>
<meta charset="utf-8">
<title>Copper Meadow – Medical Supplies</title>
<link href="https://fonts.googleapis.com/css2?family=Poppins:wght@400;500;600&family=Roboto:wght@400;500;700&display=swap" rel="stylesheet">
<style>
:root{
  --blue:#1ea0db;
  --blue-dark:#1587bd;
  --green:#7cc242;
  --green-dark:#62a82d;
  --ink:#222;
  --body:#777;
  --hero:#d7eef6;
  --grey:#f2f3f5;
  --navy:#0c1b23;
  --canvas:#e9ebee;
}
*{box-sizing:border-box;margin:0;padding:0}
html,body{width:1200px;height:2256px;overflow:hidden;background:var(--canvas);font-family:Roboto,Arial,sans-serif;color:var(--ink)}
.page{position:absolute;top:42px;width:539px;background:#fff;overflow:hidden}
.page--wave{left:40px}
.page--square{left:621px}
section,header{position:relative;overflow:hidden}
.topbar{height:21px;background:var(--blue);color:#fff;font-size:5.5px;font-weight:700;display:flex;justify-content:space-between;align-items:center;padding:0 50px;text-transform:uppercase}
.topbar .phone{display:flex;align-items:center;gap:3px}
.nav{height:31px;display:flex;align-items:center;justify-content:space-between;padding:0 52px;font-size:5.5px;font-weight:700;text-transform:uppercase}
.nav ul{display:flex;align-items:center;gap:16px;list-style:none}
.nav .active{color:var(--blue);border-bottom:1px solid var(--blue);padding-bottom:2px}
.brand{font-family:Poppins,sans-serif;font-weight:500;font-size:10.5px;color:var(--blue);letter-spacing:.3px;display:flex;align-items:center;gap:4px}
.brand i{width:6px;height:6px;border-radius:50%;background:var(--green);display:inline-block}
.btn{display:inline-flex;align-items:center;gap:4px;background:var(--green);color:#fff;font-size:5.5px;font-weight:700;text-transform:uppercase;border-radius:10px;padding:5px 10px}
.btn b{width:5px;height:5px;border-radius:50%;background:#fff;display:inline-block}
.ph{position:absolute;display:block}
.eyebrow{font-size:5.5px;color:var(--blue);font-weight:500;text-align:center}
.title{font-family:Poppins,sans-serif;font-weight:500;font-size:12.5px;text-align:center;text-transform:uppercase;margin-top:4px}
.rule{width:14px;height:1px;background:var(--blue);margin:6px auto 0}
.left .eyebrow,.left .title{text-align:left}.left .rule{margin-left:0}
.text{font-size:5.8px;line-height:1.75;color:var(--body);text-align:justify}
.hero{background:linear-gradient(180deg,#d3ecf5,#e4f3f8)}
.hero h1{font-family:Poppins,sans-serif;font-weight:600;font-size:18.5px;line-height:1.35;text-transform:uppercase}
.hero .wave{position:absolute;left:0;bottom:0}
.hero-scene{position:absolute;inset:0;background:radial-gradient(ellipse at 50% 45%,#e3f3f8 0,#d2ebf4 60%,#c9e5ef 100%)}
.badge{position:absolute;background:var(--blue);color:#fff;text-align:center;font-family:Poppins,sans-serif;font-size:7px;font-weight:500;line-height:1.3}
.badge small{display:block;font-family:Roboto,sans-serif;font-size:5px;font-weight:400;opacity:.85;margin-top:3px}
.photo{background:linear-gradient(135deg,#9fb9c9,#5f7e95)}
.featured{background:var(--grey)}
.cards{display:flex;gap:6px;justify-content:center}
.card{width:106px;background:#fff;text-align:center;position:relative;overflow:hidden}
.card h3{font-family:Roboto,sans-serif;font-size:7.5px;font-weight:700;margin-top:12px}
.card .rule{width:10px;background:var(--green);margin-top:4px}
.card p{font-size:5.3px;line-height:1.6;color:var(--body);padding:0 7px;margin-top:5px;text-align:justify;text-align-last:center}
.card .blobs{position:absolute;left:0;bottom:0}
.card .ph{left:26px;bottom:12px;width:54px;height:60px;border-radius:6px;background:linear-gradient(180deg,#e6e9ee,#b9c3cd)}
.partners{display:flex;gap:8px;justify-content:center;margin-top:18px}
.partner{width:84px;height:44px;border-radius:6px;background:#f4fbfd;box-shadow:0 1px 4px rgba(30,160,219,.18);display:flex;align-items:center;justify-content:center;gap:5px}
.partner span{width:16px;height:16px;border-radius:50%;background:#c7e5f1}
.partner em{width:32px;height:5px;border-radius:3px;background:#d8eaf1}
.why{background:linear-gradient(180deg,#eef0f2 0,#eef0f2 45%,#fff 45%)}
.feature{position:absolute;color:#fff;text-align:center;display:flex;flex-direction:column;align-items:center;justify-content:center;padding:0 34px}
.feature h3{font-family:Poppins,sans-serif;font-weight:500;font-size:11px;text-transform:uppercase;margin-top:10px}
.feature .rule{background:#fff}
.feature p{font-size:5.5px;line-height:1.75;margin-top:10px;text-align:justify;text-align-last:center;opacity:.95}
.feature a{font-size:5px;font-weight:700;text-decoration:underline;margin-top:7px;text-transform:uppercase}
.feature .icon{width:34px;height:30px;border-radius:6px;background:rgba(255,255,255,.85)}
.feature--blue{background:linear-gradient(160deg,#1fa3dc,#2bb5a9)}
.feature--green{background:linear-gradient(160deg,#84c741,#5db247)}
.news{display:flex;gap:12px;justify-content:center;margin-top:24px}
.post{width:141px}
.post .img{height:101px;position:relative;background:linear-gradient(135deg,#b6c9d6,#6d8aa0)}
.post .date{position:absolute;left:15px;top:-1px;width:17px;background:var(--navy);color:#fff;text-align:center;font-size:6px;font-weight:700;line-height:1.2;padding:2px 0}
.post .date small{display:block;background:var(--blue);font-size:4px;padding:1px 0}
.post h4{font-size:6.5px;font-weight:700;margin:11px 11px 0}
.post .rule{margin:6px 11px 0;width:12px}
.post p{font-size:5.4px;line-height:1.7;color:var(--body);margin:6px 11px 0}
.more{display:block;font-size:5px;font-weight:700;color:var(--blue);text-decoration:underline;margin:7px 11px 0}
.contact{background:linear-gradient(180deg,#7cc242,#8dcb3f);color:#fff}
.contact .eyebrow,.contact .title{color:#fff}.contact .rule{background:#fff}
.form{display:flex;gap:12px;justify-content:center}
.col{display:flex;flex-direction:column;gap:7px;width:203px}
.field{height:22px;background:#fff;color:#666;font-size:5.5px;padding:0 8px;display:flex;align-items:center;border:1px solid #e3e3e3}
.field--area{height:80px;align-items:flex-start;padding-top:8px}
.submit{width:80px;height:22px;background:var(--blue);color:#fff;font-size:7px;font-weight:700;display:flex;align-items:center;justify-content:center}
.footer{background:var(--navy);color:#fff}
.fcols{display:flex;padding:0 50px;justify-content:space-between}
.fcols h5{font-size:6px;font-weight:700;text-transform:uppercase;margin-bottom:10px}
.fcols p,.fcols li{font-size:5.5px;line-height:1.6;color:#d8dde0}
.social{display:flex;gap:4px;margin-top:10px}
.social span{width:13px;height:13px;border:1px solid var(--blue);border-radius:50%}
.ci{display:flex;gap:8px;margin-bottom:8px}
.ci svg{flex:none;margin-top:1px}
.input{height:18px;background:#fff;color:#777;font-size:5.5px;display:flex;align-items:center;padding:0 7px;margin-top:6px;width:131px}
.sub{display:inline-block;background:var(--blue);color:#fff;font-size:5.5px;font-weight:700;border-radius:9px;padding:5px 14px;margin-top:7px;text-transform:uppercase}
.links{list-style:none}
.links li{margin-bottom:5px}
.links li::before{content:"»";margin-right:9px}
.bottom{height:20px;background:var(--blue);color:#fff;font-size:6px;display:flex;align-items:center;justify-content:center}
</style>
</head>
<body>

<div class="page page--wave">
  <div class="topbar"><span>Welcome to Copper Meadow</span><span class="phone"><svg width="6" height="6" viewBox="0 0 10 10"><path d="M2 0l2 2-1 2a7 7 0 003 3l2-1 2 2-2 2C4 10 0 6 0 2z" fill="#fff"/></svg>Contact us &nbsp;|&nbsp; +1 555 010 0199</span></div>
  <header class="nav">
    <ul><li class="active">Home</li><li>About</li><li>Our Products</li></ul>
    <div class="brand">COPPER <i></i> MEADOW</div>
    <ul><li>News</li><li>Contact</li><li><span class="btn">Log in <b></b></span></li></ul>
  </header>

  <section class="hero" style="height:292px">
    <span class="hero-scene" role="img" aria-label="Medical supplies arranged around the headline: capsules, gloves, stethoscope, thermometer, tweezers and face mask"></span>
    <div style="position:absolute;left:0;right:0;top:64px;text-align:center">
      <h1>Time to get all medical<br>needs for you</h1>
      <p class="text" style="text-align:center;margin:8px auto 0;width:250px">Sed ut perspiciatis unde omnis iste natus error sit voluptatem accusantium doloremque laudantium, totam rem aperiam, eaque ipsa quae</p>
      <div style="margin-top:10px"><span class="btn">Get started <b></b></span></div>
    </div>
    <svg class="wave" width="539" height="80" viewBox="0 0 539 80" preserveAspectRatio="none">
      <path d="M0 80V30C130 95 330 60 539 0V80Z" fill="#fff"/>
      <path d="M60 58C190 88 350 56 539 6" fill="none" stroke="var(--blue)" stroke-width="3"/>
      <path d="M0 42C120 95 330 64 539 12" fill="none" stroke="var(--green)" stroke-width="4"/>
    </svg>
  </section>

  <section style="height:240px">
    <span class="ph photo" role="img" aria-label="Modern operating room" style="left:141px;top:18px;width:98px;height:98px;border-radius:50%"></span>
    <span class="ph photo" role="img" aria-label="Surgical lamps over a bed" style="left:54px;top:70px;width:98px;height:98px;border-radius:50%"></span>
    <span class="ph photo" role="img" aria-label="Hospital operating theatre" style="left:136px;top:122px;width:98px;height:98px;border-radius:50%"></span>
    <div class="badge" style="left:127px;top:86px;width:52px;height:52px;border-radius:50%;padding-top:13px">Hospital<br>Equipment<small>Available Here !</small></div>
    <div class="left" style="position:absolute;left:297px;top:34px;width:185px">
      <p class="eyebrow">Who We Are</p>
      <h2 class="title">About us</h2>
      <div class="rule"></div>
      <p class="text" style="margin-top:12px">At vero eos et accusamus et iusto odio dignissimos ducimus qui blanditiis praesentium voluptatum deleniti atque corrupti quos dolores et quas molestias excepturi sint occaecati cupiditate non provident, similique sunt in culpa qui officia deserunt mollitia animi, id est laborum et dolorum fuga. Et harum quidem rerum facilis est et expedita distinctio. Nam libero tempore, cum soluta nobis est eligendi optio cumque nihil impedit quo minus id quod maxime placeat facere possimus, omnis voluptas assumenda est, omnis dolor repellendus. Temporibus autem quibusdam et aut officiis debitis</p>
      <div style="margin-top:13px"><span class="btn">Learn more <b></b></span></div>
    </div>
  </section>

  <section class="featured" style="height:369px;background:linear-gradient(180deg,#fff 0,#fff 8%,var(--grey) 8%,var(--grey) 80%,#fff 80%)">
    <svg class="ph" style="left:0;top:0" width="539" height="80" viewBox="0 0 539 80" preserveAspectRatio="none">
      <path d="M0 0H539V10C400 10 300 80 150 70 80 66 30 50 0 40Z" fill="#fff"/>
      <path d="M0 40C60 66 120 72 190 64 330 48 420 0 539 22" fill="none" stroke="var(--green)" stroke-width="4"/>
      <path d="M170 64C320 40 430 -6 539 8" fill="none" stroke="var(--blue)" stroke-width="3"/>
    </svg>
    <div style="position:relative;padding-top:84px">
      <p class="eyebrow">Products</p>
      <h2 class="title">Featured products</h2>
      <div class="rule"></div>
      <div class="cards" style="margin-top:16px">
        <article class="card" style="height:150px"><h3>Product Title</h3><div class="rule"></div><p>Sed ut perspiciatis unde omnis iste natus error sit voluptatem accusantium dolore</p><svg class="blobs" width="106" height="40"><circle cx="20" cy="60" r="48" fill="var(--blue)"/><circle cx="92" cy="62" r="46" fill="var(--green)"/></svg><span class="ph" role="img" aria-label="Hand sanitizer bottles"></span></article>
        <article class="card" style="height:150px"><h3>Product Title</h3><div class="rule"></div><p>Sed ut perspiciatis unde omnis iste natus error sit voluptatem accusantium dolore</p><svg class="blobs" width="106" height="40"><circle cx="20" cy="60" r="48" fill="var(--green)"/><circle cx="92" cy="62" r="46" fill="var(--green)" opacity=".8"/></svg><span class="ph" role="img" aria-label="Anaesthesia machine"></span></article>
        <article class="card" style="height:150px"><h3>Product Title</h3><div class="rule"></div><p>Sed ut perspiciatis unde omnis iste natus error sit voluptatem accusantium dolore</p><svg class="blobs" width="106" height="40"><circle cx="20" cy="60" r="48" fill="var(--blue)"/><circle cx="92" cy="62" r="46" fill="var(--blue)"/></svg><span class="ph" role="img" aria-label="Vaccine vial"></span></article>
        <article class="card" style="height:150px"><h3>Product Title</h3><div class="rule"></div><p>Sed ut perspiciatis unde omnis iste natus error sit voluptatem accusantium dolore</p><svg class="blobs" width="106" height="40"><circle cx="20" cy="60" r="48" fill="var(--blue)"/><circle cx="92" cy="62" r="46" fill="var(--green)"/></svg><span class="ph" role="img" aria-label="Blood pressure monitor"></span></article>
      </div>
    </div>
    <svg class="ph" style="left:0;bottom:0" width="539" height="95" viewBox="0 0 539 95" preserveAspectRatio="none">
      <path d="M0 40C100 90 200 95 300 60 400 25 470 10 539 20V95H0Z" fill="#fff"/>
      <path d="M0 30C100 85 210 92 320 52 410 20 480 14 539 26" fill="none" stroke="var(--blue)" stroke-width="4"/>
      <path d="M280 60C380 20 460 0 539 6" fill="none" stroke="var(--green)" stroke-width="4"/>
    </svg>
  </section>

  <section style="height:145px">
    <p class="eyebrow" style="margin-top:8px">Our Partners</p>
    <h2 class="title">Approved by leading health organizations</h2>
    <div class="rule"></div>
    <div class="partners">
      <div class="partner"><span></span><em></em></div><div class="partner"><span></span><em></em></div><div class="partner"><span></span><em></em></div><div class="partner"><span></span><em></em></div><div class="partner"><span></span><em></em></div>
    </div>
  </section>

  <section class="why" style="height:320px">
    <p class="eyebrow" style="margin-top:36px">Why Us</p>
    <h2 class="title">Why choose us</h2>
    <div class="rule"></div>
    <div class="feature feature--blue" style="left:70px;top:78px;width:212px;height:212px;border-radius:50%;box-shadow:0 0 0 6px #1d8fd0">
      <span class="icon" role="img" aria-label="Globe icon"></span><h3>Global Warming</h3><div class="rule"></div>
      <p>At vero eos et accusamus et iusto odio dignissimos ducimus qui blanditiis praesentium voluptatum deleniti atque corrupti quos dolores et quas molestias excepturi sint occaecati</p><a>Learn more ›</a>
    </div>
    <div class="feature feature--green" style="left:256px;top:78px;width:212px;height:212px;border-radius:50%;box-shadow:0 0 0 6px #6fb53a">
      <span class="icon" role="img" aria-label="Production line icon"></span><h3>Raw Material Shortages</h3><div class="rule"></div>
      <p>At vero eos et accusamus et iusto odio dignissimos ducimus qui blanditiis praesentium voluptatum deleniti atque corrupti quos dolores et quas molestias excepturi sint occaecati</p><a>Learn more ›</a>
    </div>
  </section>

  <section style="height:285px">
    <p class="eyebrow" style="margin-top:20px">Resources</p>
    <h2 class="title">Latest news</h2>
    <div class="rule"></div>
    <div class="news">
      <article class="post"><div class="img" role="img" aria-label="Pharmacist stocking shelves"><div class="date">01<small>JAN</small></div></div><h4>Lorem ipsum dolor sit amet</h4><div class="rule"></div><p>Sed ut perspiciatis unde omnis iste natus error sit voluptatem accusanti doloremque laudantium, totam rem aperiam</p><a class="more">Read more ›</a></article>
      <article class="post"><div class="img" role="img" aria-label="Operating room with imaging equipment"><div class="date">01<small>JAN</small></div></div><h4>Lorem ipsum dolor sit amet</h4><div class="rule"></div><p>Sed ut perspiciatis unde omnis iste natus error sit voluptatem accusanti doloremque laudantium, totam rem aperiam</p><a class="more">Read more ›</a></article>
      <article class="post"><div class="img" role="img" aria-label="Pharmacist in a drug store"><div class="date">01<small>JAN</small></div></div><h4>Lorem ipsum dolor sit amet</h4><div class="rule"></div><p>Sed ut perspiciatis unde omnis iste natus error sit voluptatem accusanti doloremque laudantium, totam rem aperiam</p><a class="more">Read more ›</a></article>
    </div>
  </section>

  <section class="contact" style="height:315px">
    <p class="eyebrow" style="margin-top:38px">Request &nbsp;A Quote</p>
    <h2 class="title">Get in touch</h2>
    <div class="rule"></div>
    <div class="form" style="margin-top:22px">
      <div class="col"><div class="field">Name *</div><div class="field">Phone *</div><div class="field">Email *</div><div class="field">Company *</div></div>
      <div class="col"><div class="field field--area">Message</div><div class="submit">SUBMIT</div></div>
    </div>
    <svg class="ph" style="left:0;bottom:0" width="539" height="70" viewBox="0 0 539 70" preserveAspectRatio="none">
      <path d="M0 70V50C150 -10 360 50 539 20V70Z" fill="var(--navy)"/>
      <path d="M0 44C160 -14 360 44 539 14" fill="none" stroke="#fff" stroke-width="3"/>
      <path d="M170 12C300 20 420 30 539 10" fill="none" stroke="var(--blue)" stroke-width="3"/>
    </svg>
  </section>

  <footer class="footer" style="height:136px">
    <div class="fcols" style="padding-top:4px">
      <div style="width:105px"><div class="brand" style="color:var(--blue);font-size:11px;margin-top:4px">COPPER <i></i> MEADOW</div><p style="margin-top:8px">At vero eos et accusamus et iusto odio dignissimos ducimus qui blanditiis praesentium</p><div class="social"><span></span><span></span><span></span><span></span></div></div>
      <div style="width:100px"><h5>Contact us</h5>
        <div class="ci"><svg width="6" height="8" viewBox="0 0 6 8"><path d="M3 0a3 3 0 013 3c0 2-3 5-3 5S0 5 0 3a3 3 0 013-3z" fill="#fff"/></svg><p>147 , Lorem Ipsum Dolor<br>United States</p></div>
        <div class="ci"><svg width="6" height="6" viewBox="0 0 10 10"><path d="M2 0l2 2-1 2a7 7 0 003 3l2-1 2 2-2 2C4 10 0 6 0 2z" fill="#fff"/></svg><p>Phone No :<br>+1 555 010 0199</p></div>
        <div class="ci"><svg width="7" height="5" viewBox="0 0 7 5"><rect width="7" height="5" fill="#fff"/><path d="M0 0l3.5 3L7 0" fill="none" stroke="var(--navy)" stroke-width=".8"/></svg><p>Email :<br>info@coppermeadow.com</p></div>
      </div>
      <div style="width:135px"><h5>Sign up for newsletter</h5><p>excepteur sint occaecat cupidatat non proident, sunt in culpa qui officia</p><div class="input">Enter email</div><span class="sub">Subscribe</span></div>
      <div><h5>Quick links</h5><ul class="links"><li>Home</li><li>About Us</li><li>Our Products</li><li>Latest News</li><li>Contact</li></ul></div>
    </div>
  </footer>
  <div class="bottom">Copper Meadow © 2022 All Rights Reserved | Privacy Policy | Terms &amp; Condition</div>
</div>

<div class="page page--square">
  <div class="topbar"><span>Welcome to Copper Meadow</span><span class="phone"><svg width="6" height="6" viewBox="0 0 10 10"><path d="M2 0l2 2-1 2a7 7 0 003 3l2-1 2 2-2 2C4 10 0 6 0 2z" fill="#fff"/></svg>Contact us &nbsp;|&nbsp; +1 555 010 0199</span></div>
  <header class="nav">
    <ul><li class="active">Home</li><li>About</li><li>Our Products</li></ul>
    <div class="brand">COPPER <i></i> MEADOW</div>
    <ul><li>News</li><li>Contact</li><li><span class="btn">Log in <b></b></span></li></ul>
  </header>

  <section class="hero" style="height:250px">
    <div style="position:absolute;left:50px;top:70px;width:250px">
      <h1>Time to get all medical<br>needs for you</h1>
      <p class="text" style="margin-top:10px;text-align:left">Sed ut perspiciatis unde omnis iste natus error sit voluptatem accusantium doloremque laudantium, totam rem aperiam, eaque ipsa quae</p>
      <div style="margin-top:10px"><span class="btn">Get started <b></b></span></div>
    </div>
    <span class="ph" role="img" aria-label="Anaesthesia workstation" style="left:337px;top:40px;width:150px;height:205px;border-radius:10px;background:linear-gradient(180deg,#f1f3f5,#c7cfd7)"></span>
  </section>

  <section style="height:298px">
    <span class="ph photo" role="img" aria-label="Hospital operating room" style="left:50px;top:70px;width:206px;height:179px"></span>
    <div class="badge" style="left:190px;top:186px;width:62px;height:60px;padding-top:14px;box-shadow:4px 4px 0 #dfe3e6">Hospital<br>Equipment<small>Available Here !</small></div>
    <div class="left" style="position:absolute;left:297px;top:70px;width:185px">
      <p class="eyebrow">Who We Are</p>
      <h2 class="title">About us</h2>
      <div class="rule"></div>
      <p class="text" style="margin-top:12px">At vero eos et accusamus et iusto odio dignissimos ducimus qui blanditiis praesentium voluptatum deleniti atque corrupti quos dolores et quas molestias excepturi sint occaecati cupiditate non provident, similique sunt in culpa qui officia deserunt mollitia animi, id est laborum et dolorum fuga. Et harum quidem rerum facilis est et expedita distinctio. Nam libero tempore, cum soluta nobis est eligendi optio cumque nihil impedit quo minus id quod maxime placeat facere possimus, omnis voluptas assumenda est, omnis dolor repellendus. Temporibus autem quibusdam et aut officiis debitis</p>
      <div style="margin-top:13px"><span class="btn">Learn more <b></b></span></div>
    </div>
  </section>

  <section class="featured" style="height:275px">
    <p class="eyebrow" style="margin-top:32px">Products</p>
    <h2 class="title">Featured products</h2>
    <div class="rule"></div>
    <div class="cards" style="margin-top:16px">
      <article class="card" style="height:150px"><h3>Product Title</h3><div class="rule"></div><p>Sed ut perspiciatis unde omnis iste natus error sit voluptatem accusantium dolore</p><svg class="blobs" width="106" height="40"><circle cx="20" cy="60" r="48" fill="var(--blue)"/><circle cx="92" cy="62" r="46" fill="var(--green)"/></svg><span class="ph" role="img" aria-label="Hand sanitizer bottles"></span></article>
      <article class="card" style="height:150px"><h3>Product Title</h3><div class="rule"></div><p>Sed ut perspiciatis unde omnis iste natus error sit voluptatem accusantium dolore</p><svg class="blobs" width="106" height="40"><circle cx="20" cy="60" r="48" fill="var(--green)"/><circle cx="92" cy="62" r="46" fill="var(--green)" opacity=".8"/></svg><span class="ph" role="img" aria-label="Anaesthesia machine"></span></article>
      <article class="card" style="height:150px"><h3>Product Title</h3><div class="rule"></div><p>Sed ut perspiciatis unde omnis iste natus error sit voluptatem accusantium dolore</p><svg class="blobs" width="106" height="40"><circle cx="20" cy="60" r="48" fill="var(--blue)"/><circle cx="92" cy="62" r="46" fill="var(--blue)"/></svg><span class="ph" role="img" aria-label="Vaccine vial"></span></article>
      <article class="card" style="height:150px"><h3>Product Title</h3><div class="rule"></div><p>Sed ut perspiciatis unde omnis iste natus error sit voluptatem accusantium dolore</p><svg class="blobs" width="106" height="40"><circle cx="20" cy="60" r="48" fill="var(--blue)"/><circle cx="92" cy="62" r="46" fill="var(--green)"/></svg><span class="ph" role="img" aria-label="Blood pressure monitor"></span></article>
    </div>
  </section>

  <section style="height:186px">
    <p class="eyebrow" style="margin-top:46px">Our Partners</p>
    <h2 class="title">Approved by leading health organizations</h2>
    <div class="partners" style="margin-top:16px">
      <div class="partner"><span></span><em></em></div><div class="partner"><span></span><em></em></div><div class="partner"><span></span><em></em></div><div class="partner"><span></span><em></em></div><div class="partner"><span></span><em></em></div>
    </div>
  </section>

  <section class="why" style="height:335px">
    <p class="eyebrow" style="margin-top:28px">Why Us</p>
    <h2 class="title">Why choose us</h2>
    <div class="rule"></div>
    <div class="feature feature--blue" style="left:45px;top:80px;width:214px;height:214px;box-shadow:0 0 0 6px #1d8fd0 inset">
      <span class="icon" role="img" aria-label="Globe icon"></span><h3>Global Warming</h3><div class="rule"></div>
      <p>At vero eos et accusamus et iusto odio dignissimos ducimus qui blanditiis praesentium voluptatum deleniti atque corrupti quos dolores et quas molestias excepturi sint occaecati</p><a>Learn more ›</a>
    </div>
    <div class="feature feature--green" style="left:280px;top:80px;width:214px;height:214px;box-shadow:0 0 0 6px #6fb53a inset">
      <span class="icon" role="img" aria-label="Production line icon"></span><h3>Raw Material Shortages</h3><div class="rule"></div>
      <p>At vero eos et accusamus et iusto odio dignissimos ducimus qui blanditiis praesentium voluptatum deleniti atque corrupti quos dolores et quas molestias excepturi sint occaecati</p><a>Learn more ›</a>
    </div>
  </section>

  <section style="height:272px">
    <p class="eyebrow" style="margin-top:8px">Resources</p>
    <h2 class="title">Latest news</h2>
    <div class="rule"></div>
    <div class="news" style="margin-top:16px">
      <article class="post"><div class="img" role="img" aria-label="Pharmacist stocking shelves"><div class="date">01<small>JAN</small></div></div><h4>Lorem ipsum dolor sit amet</h4><div class="rule"></div><p>Sed ut perspiciatis unde omnis iste natus error sit voluptatem accusanti doloremque laudantium, totam rem aperiam</p><a class="more">Read more ›</a></article>
      <article class="post"><div class="img" role="img" aria-label="Operating room with imaging equipment"><div class="date">01<small>JAN</small></div></div><h4>Lorem ipsum dolor sit amet</h4><div class="rule"></div><p>Sed ut perspiciatis unde omnis iste natus error sit voluptatem accusanti doloremque laudantium, totam rem aperiam</p><a class="more">Read more ›</a></article>
      <article class="post"><div class="img" role="img" aria-label="Pharmacist in a drug store"><div class="date">01<small>JAN</small></div></div><h4>Lorem ipsum dolor sit amet</h4><div class="rule"></div><p>Sed ut perspiciatis unde omnis iste natus error sit voluptatem accusanti doloremque laudantium, totam rem aperiam</p><a class="more">Read more ›</a></article>
    </div>
  </section>

  <section class="contact" style="height:251px">
    <p class="eyebrow" style="margin-top:36px">Request &nbsp;A Quote</p>
    <h2 class="title">Get in touch</h2>
    <div class="rule"></div>
    <div class="form" style="margin-top:20px">
      <div class="col"><div class="field">Name *</div><div class="field">Phone *</div><div class="field">Email *</div><div class="field">Company *</div></div>
      <div class="col"><div class="field field--area">Message</div><div class="submit">SUBMIT</div></div>
    </div>
  </section>

  <footer class="footer" style="height:161px">
    <div class="fcols" style="padding-top:36px">
      <div style="width:105px"><div class="brand" style="color:var(--blue);font-size:11px;margin-top:10px">COPPER <i></i> MEADOW</div><p style="margin-top:8px">At vero eos et accusamus et iusto odio dignissimos ducimus qui blanditiis praesentium</p><div class="social"><span></span><span></span><span></span><span></span></div></div>
      <div style="width:100px"><h5>Contact us</h5>
        <div class="ci"><svg width="6" height="8" viewBox="0 0 6 8"><path d="M3 0a3 3 0 013 3c0 2-3 5-3 5S0 5 0 3a3 3 0 013-3z" fill="#fff"/></svg><p>147 , Lorem Ipsum Dolor<br>United States</p></div>
        <div class="ci"><svg width="6" height="6" viewBox="0 0 10 10"><path d="M2 0l2 2-1 2a7 7 0 003 3l2-1 2 2-2 2C4 10 0 6 0 2z" fill="#fff"/></svg><p>Phone No :<br>+1 555 010 0199</p></div>
        <div class="ci"><svg width="7" height="5" viewBox="0 0 7 5"><rect width="7" height="5" fill="#fff"/><path d="M0 0l3.5 3L7 0" fill="none" stroke="var(--navy)" stroke-width=".8"/></svg><p>Email :<br>info@coppermeadow.com</p></div>
      </div>
      <div style="width:135px"><h5>Sign up for newsletter</h5><p>excepteur sint occaecat cupidatat non proident, sunt in culpa qui officia</p><div class="input">Enter email</div><span class="sub">Subscribe</span></div>
      <div><h5>Quick links</h5><ul class="links"><li>Home</li><li>About Us</li><li>Our Products</li><li>Latest News</li><li>Contact</li></ul></div>
    </div>
  </footer>
  <div class="bottom">Copper Meadow © 2022 All Rights Reserved | Privacy Policy | Terms &amp; Condition</div>
</div>

</body>
</html>
```